Business Cards

Business cards (double-sided) to be handed out to clients and potential clients, with contact details, logo .

Target Market(s)

Small to medium size businesses

Industry/Entity Type

Accountants

Contact Information for Business Card

Brightwater Ledger & Counsel Ltd

Colors

Designer to choose only greyscale colors for use in the design.

Requirements
Must have
• Name, Title, Address, Phone number, Email, Website
Nice to have
• Modern, clean lines, classy
Should not have
• Business cards to be double-sided. Form keeps reverting to single-sided.

```html
<!DOCTYPE html>
<html lang="en">
<head>
<meta charset="utf-8">
<title>Brightwater Ledger &amp; Counsel Ltd — Business Card</title>
<link rel="stylesheet" href="https://fonts.googleapis.com/css2?family=Montserrat:wght@400;500;700&display=swap">
<style>
  :root {
    --backdrop: #2b2d2c;
    --card: #ffffff;
    --ink: #111111;
    --grey: #9a9a9a;
    --black: #0c0c0c;
  }
  * { margin: 0; padding: 0; box-sizing: border-box; }
  html, body { width: 1200px; height: 910px; overflow: hidden; }
  body {
    background: var(--backdrop);
    font-family: "Montserrat", sans-serif;
    color: var(--ink);
    position: relative;
  }
  .card {
    position: absolute;
    width: 620px;
    height: 354px;
    background: var(--card);
    border-radius: 22px;
    overflow: hidden;
    box-shadow: 0 14px 30px rgba(0,0,0,0.45);
  }
  .card--front { left: 110px; top: 70px; }
  .card--back { left: 470px; top: 486px; }

  .wordmark {
    font-weight: 500;
    color: var(--ink);
    text-transform: uppercase;
    letter-spacing: 0.14em;
    line-height: 1.35;
  }
  .card--front .wordmark {
    position: absolute;
    left: 0; right: 0; top: 50%;
    transform: translateY(-50%);
    text-align: center;
    font-size: 24px;
  }
  .card--back .wordmark {
    position: absolute;
    left: 40px; top: 140px;
    width: 230px;
    font-size: 17px;
  }

  .divider {
    position: absolute;
    left: 300px; top: 70px;
    width: 1px; height: 190px;
    background: var(--ink);
  }
  .details {
    position: absolute;
    left: 322px; top: 62px;
    font-size: 15px;
    line-height: 1.3;
  }
  .details__name { font-weight: 700; font-size: 17px; letter-spacing: 0.02em; }
  .details__title { margin-left: 10px; margin-bottom: 12px; }
  .details__address { margin-bottom: 12px; }
  .contact { list-style: none; }
  .contact li { display: flex; align-items: center; gap: 8px; margin-bottom: 3px; }
  .contact svg { width: 15px; height: 15px; flex: none; }

  .edge-bands { position: absolute; left: 0; bottom: 0; width: 620px; height: 22px; }
</style>
</head>
<body>
  <section class="card card--front" aria-label="Card front">
    <p class="wordmark">Brightwater Ledger<br>&amp; Counsel Ltd</p>
  </section>

  <section class="card card--back" aria-label="Card back">
    <p class="wordmark">Brightwater Ledger<br>&amp; Counsel Ltd</p>
    <div class="divider"></div>
    <div class="details">
      <p class="details__name">DANA WHITLOCK</p>
      <p class="details__title">Co-Founder</p>
      <p class="details__address">42 Harbor Lane 5<br>Eastfield, NY 10422</p>
      <ul class="contact">
        <li>
          <svg viewBox="0 0 16 16" aria-hidden="true"><path d="M2 5c0-2 2-3 6-3s6 1 6 3v1h-3V5H5v1H2z M4 8h8l1 6H3z" fill="currentColor"/></svg>
          555-210-4471
        </li>
        <li>
          <svg viewBox="0 0 16 16" aria-hidden="true"><rect x="1" y="3" width="14" height="10" fill="currentColor"/><path d="M1 3l7 6 7-6" fill="none" stroke="#fff" stroke-width="1.2"/></svg>
          hello@brightwaterledger.com
        </li>
        <li>
          <svg viewBox="0 0 16 16" aria-hidden="true"><circle cx="8" cy="8" r="7" fill="currentColor"/><path d="M1 8h14M8 1c3 3 3 11 0 14M8 1c-3 3-3 11 0 14" fill="none" stroke="#fff" stroke-width="1"/></svg>
          www.brightwaterledger.com
        </li>
      </ul>
    </div>
    <svg class="edge-bands" viewBox="0 0 620 22" preserveAspectRatio="none" aria-hidden="true">
      <polygon points="0,10 400,10 396,22 0,22" fill="var(--black)"/>
      <polygon points="406,4 620,4 620,22 400,22" fill="var(--grey)"/>
    </svg>
  </section>
</body>
</html>
```